Harborline Security and Surveillance Business Card

Business Card Design - Company Name:Freedom Security and SurveillanceWe are a Security Systems Integrator Specializing in Security Systems/ Video Surveillance and Access Control. Our areas of expertise are:Security SystemsVideo SurveillanceAccess ControlFire Alarm SystemsNetwork CablingCellular BoostersMy input is the Front of the Card is: logo, name of Business, My Name, Phone Number, and email.Rear of Card is the 6 areas of expertise, I just dont want the front to be very busy.
Name: Tom Jenner
Title: President
Email: tom@harborlinesecuritysys.example
website: harborlinesecuritysys.example

```html
<!DOCTYPE html>
<html lang="en">
<head>
<meta charset="utf-8">
<title>Harborline Security and Surveillance Business Card</title>
<link href="https://fonts.googleapis.com/css2?family=Roboto:wght@400;500&family=Oswald:wght@600&display=swap" rel="stylesheet">
<style>
  :root {
    --bg: #d9d9db;
    --card: #1c1c1d;
    --card-edge: #0d0d0d;
    --blue: #0a5fc4;
    --silver: #c9cacc;
    --text: #e6e6e6;
    --muted: #a9aaac;
  }
  * { box-sizing: border-box; margin: 0; padding: 0; }
  html, body { width: 1200px; height: 1200px; overflow: hidden; background: var(--bg); }
  body { font-family: "Roboto", Arial, sans-serif; position: relative; }

  .card {
    position: absolute; left: 150px; width: 900px; height: 514px;
    border-radius: 28px;
    background: linear-gradient(115deg, var(--card-edge) 0%, var(--card) 45%, #242425 100%);
    box-shadow: 0 18px 40px rgba(0,0,0,.35);
    overflow: hidden;
  }
  .card--back { top: 70px; }
  .card--front { top: 616px; }

  /* back */
  .wordmark { position: absolute; top: 78px; left: 0; right: 0; text-align: center; }
  .wordmark__name {
    display: inline-flex; align-items: center; gap: 14px;
    color: var(--blue); font-weight: 500; font-size: 44px; letter-spacing: 7px; text-transform: uppercase;
  }
  .wordmark__dot { width: 34px; height: 34px; border-radius: 50%; background: var(--blue); }
  .wordmark__sub {
    display: flex; align-items: center; justify-content: center; gap: 16px; margin-top: 6px;
    color: var(--silver); font-size: 15px; letter-spacing: 9px; text-transform: uppercase;
  }
  .wordmark__rule { width: 120px; height: 2px; background: var(--muted); }

  .services {
    position: absolute; top: 258px; left: 40px; right: 40px;
    display: flex; justify-content: space-between; list-style: none;
  }
  .service { width: 150px; text-align: center; color: var(--text); font-size: 15px; line-height: 1.25; }
  .service__badge {
    width: 92px; height: 92px; margin: 0 auto 12px; border-radius: 50%;
    border: 2px solid var(--blue); display: flex; align-items: center; justify-content: center;
  }
  .service__art { width: 54px; height: 54px; border-radius: 50%; background: radial-gradient(circle, #1f6fd1, #0a4fa3); }

  /* front */
  .front-mark {
    position: absolute; left: 60px; top: 60px; width: 420px; height: 394px;
    display: flex; flex-direction: column; justify-content: center;
    color: var(--blue); font-weight: 500; font-size: 56px; line-height: 1.05; letter-spacing: 2px;
  }
  .contact { position: absolute; right: 80px; bottom: 70px; text-align: right; }
  .contact__name { font-family: "Oswald", "Arial Narrow", sans-serif; font-weight: 600; font-size: 44px; color: var(--blue); text-transform: uppercase; line-height: 1; }
  .contact__title { color: var(--muted); font-size: 22px; margin: 4px 0 20px; }
  .contact__block { display: flex; gap: 14px; align-items: stretch; }
  .contact__lines { display: flex; flex-direction: column; gap: 10px; }
  .contact__line { display: flex; align-items: center; justify-content: flex-end; gap: 12px; color: var(--silver); font-size: 19px; }
  .contact__line .accent { color: var(--blue); }
  .contact__rule { width: 2px; background: var(--blue); }
  .icon { width: 20px; height: 20px; flex: none; }
</style>
</head>
<body>

<section class="card card--back" aria-label="Card back">
  <div class="wordmark">
    <div class="wordmark__name"><span class="wordmark__dot"></span>Harborline Security</div>
    <div class="wordmark__sub"><span class="wordmark__rule"></span>and Surveillance<span class="wordmark__rule"></span></div>
  </div>
  <ul class="services">
    <li class="service"><div class="service__badge"><div class="service__art" role="img" aria-label="Security camera icon"></div></div>Video<br>Surveillance</li>
    <li class="service"><div class="service__badge"><div class="service__art" role="img" aria-label="Keypad and access card icon"></div></div>Access Control</li>
    <li class="service"><div class="service__badge"><div class="service__art" role="img" aria-label="Fire alarm icon"></div></div>Fire Alarm<br>Systems</li>
    <li class="service"><div class="service__badge"><div class="service__art" role="img" aria-label="Network cable icon"></div></div>Network Cabling</li>
    <li class="service"><div class="service__badge"><div class="service__art" role="img" aria-label="Cell tower icon"></div></div>Cellular<br>Boosters</li>
  </ul>
</section>

<section class="card card--front" aria-label="Card front">
  <div class="front-mark">Harborline<br>Security and<br>Surveillance</div>
  <div class="contact">
    <div class="contact__name">Tom Jenner</div>
    <div class="contact__title">President</div>
    <div class="contact__block">
      <div class="contact__lines">
        <div class="contact__line">tom@harborlinesecuritysys.example
          <svg class="icon" viewBox="0 0 20 20"><rect x="2" y="5" width="16" height="11" fill="none" stroke="#0a5fc4" stroke-width="1.8"/><path d="M2 5l8 6 8-6" fill="none" stroke="#0a5fc4" stroke-width="1.8"/></svg>
        </div>
        <div class="contact__line">www.<span class="accent">harborlinesecuritysys</span>.example
          <svg class="icon" viewBox="0 0 20 20" fill="none" stroke="#0a5fc4" stroke-width="1.6"><circle cx="10" cy="10" r="8"/><ellipse cx="10" cy="10" rx="3.5" ry="8"/><path d="M2 10h16M3.5 6h13M3.5 14h13"/></svg>
        </div>
      </div>
      <div class="contact__rule"></div>
    </div>
  </div>
</section>

</body>
</html>
```